Congressional Website with splash page for Texas Democratic Black Woman

I would like a splash page with a turquoise shaded theme to it. My logo can be played with but the original logo is black white and red... we are now wanting a page that is in shades of turquoise with the black white and red colors. On the splash page, I want to collect volunteer information and prompt people to donate. I would like to.just have a large picture of me of some sort and then you have to click to enter the rest of the page with the issues.

Target Market(s)

Voters and Donors and democrats

Industry/Entity Type

campaign/elections

Coding

Coded - Design and coding required

Number of Pages Required

2 page

Font styles to use
Serif

Colors
0094D4
00A9DD
6FCCEA
C7EBF8
E9F6FB

Requirements
Must have
• I must have a landing page... and then it open up to the other pages.

```html
<!DOCTYPE html>
<html lang="en">
<head>
<meta charset="utf-8">
<title>Marisol Benton — Democrat for US Congress</title>
<link href="https://fonts.googleapis.com/css2?family=Oswald:wght@400;500&family=Playfair+Display:wght@400&family=Great+Vibes&family=Roboto:wght@400;500;700&display=swap" rel="stylesheet">
<style>
:root{
  --teal:#2cc4cc;
  --teal-deep:#22b6c0;
  --teal-line:#4cc3cb;
  --red:#ff0a2a;
  --white:#ffffff;
  --ink:#111111;
  --grey:#555555;
  --field:#8a8a8a;
}
*{margin:0;padding:0;box-sizing:border-box}
html,body{width:909px;height:1200px;overflow:hidden;background:var(--white)}
.page{position:relative;width:909px;height:1200px;overflow:hidden;font-family:'Roboto',sans-serif}
.hero-bg{position:absolute;left:0;top:0}
.brand{position:absolute;left:87px;top:18px;width:138px;color:var(--white)}
.brand-name{font-family:'Playfair Display',serif;font-size:20px;line-height:1;letter-spacing:.5px;white-space:nowrap}
.brand-tag{margin-top:8px;border-top:1.5px solid var(--red);border-bottom:1.5px solid var(--red);font-family:'Oswald',sans-serif;font-size:9px;font-weight:500;letter-spacing:.8px;padding:2px 3px;white-space:nowrap}
.nav{position:absolute;top:31px;left:350px;display:flex;align-items:center}
.nav a{font-family:'Oswald',sans-serif;font-size:12px;letter-spacing:2px;color:var(--white);text-decoration:none;font-weight:500}
.nav .home{position:relative}
.nav .home::after{content:"";position:absolute;left:0;right:2px;bottom:-8px;height:1.5px;background:var(--white)}
.nav .gap1{margin-left:47px}.nav .gap2{margin-left:47px}.nav .gap3{margin-left:46px}
.nav .donate-btn{margin-left:30px;border:1.5px solid var(--white);border-radius:16px;width:96px;height:31px;display:flex;align-items:center;justify-content:center}
.hero-kicker{position:absolute;left:88px;top:185px;width:254px;border-top:1.2px solid var(--white);border-bottom:1.2px solid var(--white);font-family:'Oswald',sans-serif;font-size:17px;font-weight:500;letter-spacing:2.6px;color:var(--white);padding:0 3px;line-height:25px;white-space:nowrap}
.hero-first{position:absolute;left:86px;top:204px;font-family:'Playfair Display',serif;font-size:76px;color:var(--white);line-height:1;letter-spacing:0}
.hero-last{position:absolute;left:82px;top:258px;font-family:'Great Vibes',cursive;font-size:84px;color:var(--red);line-height:1}
.enter-btn{position:absolute;left:89px;top:362px;width:170px;height:41px;background:var(--red);color:var(--white);font-family:'Oswald',sans-serif;font-size:15px;font-weight:500;letter-spacing:2px;display:flex;align-items:center;justify-content:center}
.portrait{position:absolute;left:437px;top:95px}
.donate-card{position:absolute;left:284px;top:650px;width:528px;height:313px;border:1.2px solid var(--teal-line)}
.donate-photo{position:absolute;left:80px;top:646px}
.donate-copy{position:absolute;left:433px;top:693px;width:360px}
.eyebrow{font-family:'Oswald',sans-serif;font-size:14px;letter-spacing:2.2px;color:var(--teal);font-weight:500}
.donate-title{font-family:'Playfair Display',serif;font-size:31px;color:var(--ink);line-height:1;margin-top:6px}
.donate-lead{font-size:9px;color:var(--grey);margin-top:9px}
.form{position:absolute;left:435px;top:785px;width:347px;display:grid;grid-template-columns:170px 170px;column-gap:7px;row-gap:7px}
.field{height:33px;border:1px solid var(--field);font-size:9px;color:#555;padding-left:13px;display:flex;align-items:center}
.submit{position:absolute;left:435px;top:877px;width:126px;height:39px;border:1.3px solid var(--teal);border-radius:20px;color:var(--teal);font-size:10.5px;font-weight:700;display:flex;align-items:center;justify-content:center}
.footer{position:absolute;left:0;top:1049px;width:909px;height:151px;background:linear-gradient(var(--teal),var(--teal-deep))}
.footer-nav{position:absolute;top:37px;left:0;width:909px;font-family:'Oswald',sans-serif;font-size:12px;letter-spacing:2px;color:var(--white);font-weight:500}
.footer-nav span{position:absolute;white-space:nowrap}
.copyright{position:absolute;top:65px;width:909px;text-align:center;font-size:9px;color:var(--white)}
.social{position:absolute;top:97px;left:401px;display:flex;gap:5px}
.social span{width:24px;height:24px;border-radius:50%;background:var(--white);display:block}
</style>
</head>
<body>
<div class="page">
  <svg class="hero-bg" width="909" height="600" viewBox="0 0 909 600">
    <defs>
      <linearGradient id="heroTint" x1="0" y1="0" x2="0" y2="1">
        <stop offset="0" stop-color="#2cc6cd"/>
        <stop offset="1" stop-color="#25b8c2"/>
      </linearGradient>
    </defs>
    <path d="M0,582 C150,520 300,524 450,552 S780,592 909,507 L909,0 L0,0 Z" fill="url(#heroTint)"/>
    <path d="M70,558 C200,522 330,532 470,556 S700,596 785,568" fill="none" stroke="var(--red)" stroke-width="3.5"/>
  </svg>

  <div class="brand" aria-label="Marisol Benton">
    <div class="brand-name">MARISOL BENTON</div>
    <div class="brand-tag">DEMOCRAT FOR US CONGRESS</div>
  </div>

  <nav class="nav">
    <a class="home">HOME</a>
    <a class="gap1">ABOUT US</a>
    <a class="gap2">ISSUES</a>
    <a class="gap3">VOLUNTEER</a>
    <a class="donate-btn">DONATE</a>
  </nav>

  <div class="hero-kicker">DEMOCRAT FOR US CONGRESS</div>
  <div class="hero-first">MARISOL</div>
  <div class="hero-last">Benton</div>
  <div class="enter-btn">CLICK TO ENTER</div>

  <svg class="portrait" width="410" height="410" viewBox="0 0 410 410" role="img" aria-label="Portrait photo of the candidate seated on a wooden bench">
    <defs>
      <radialGradient id="portraitFill" cx="0.5" cy="0.45" r="0.6">
        <stop offset="0" stop-color="#3a2a3a"/>
        <stop offset="0.45" stop-color="#8a5a1c"/>
        <stop offset="1" stop-color="#e0a020"/>
      </radialGradient>
    </defs>
    <circle cx="204" cy="204" r="204" fill="none" stroke="var(--white)" stroke-width="1.5"/>
    <circle cx="204" cy="204" r="196" fill="url(#portraitFill)"/>
  </svg>

  <div class="donate-card"></div>
  <svg class="donate-photo" width="332" height="332" viewBox="0 0 332 332" role="img" aria-label="Photo of a hand dropping a coin into a donation jar">
    <defs>
      <linearGradient id="jarFill" x1="0" y1="0" x2="0" y2="1">
        <stop offset="0" stop-color="#a8d84a"/>
        <stop offset="0.6" stop-color="#5e9a2e"/>
        <stop offset="1" stop-color="#d8d2c4"/>
      </linearGradient>
    </defs>
    <circle cx="166" cy="166" r="160" fill="url(#jarFill)" stroke="var(--red)" stroke-width="11"/>
  </svg>

  <div class="donate-copy">
    <div class="eyebrow">WANT TO DONATE</div>
    <div class="donate-title">DONATE NOW</div>
    <div class="donate-lead">Lorem ipsum dolor sit amet, consectetur adipiscing elit, sed do eiusmod tempor</div>
  </div>
  <div class="form">
    <div class="field">First Name</div>
    <div class="field">Last Name</div>
    <div class="field">Email</div>
    <div class="field">Phone</div>
  </div>
  <div class="submit">DONATE NOW</div>

  <footer class="footer">
    <div class="footer-nav">
      <span style="left:236px">HOME</span>
      <span style="left:317px">ABOUT US</span>
      <span style="left:423px">ISSUES</span>
      <span style="left:511px">VOLUNTEER</span>
      <span style="left:634px">DONATE</span>
    </div>
    <div class="copyright">© 2021 Marisol Benton | All Rights Reserved</div>
    <div class="social" aria-label="Social links">
      <span></span><span></span><span></span><span></span>
    </div>
  </footer>
</div>
</body>
</html>
```